Wordpress Design Project

A brand new wordpress website for my business which will replace my current site www.ferndalecomms.com.au, As i rank quite well in searlo will it be ok to keep my current URL's. I sell the following service and products

1. Voip Provider (Main service) we sell directly the the end user but also we would like to get resellers and agents to sell our services. agents selling our brand resellers sell our services branded as theirs
2. Hosted Pbx (main service) home page must push this service explaining the benifits and features that come with a hosted pbx, we also have business plans based on number of extensions (phones) the customer requires
3. Nolvar IP Pbx (product) only selling IP Pbx and selected software
4. Dalqon IP Pbx (product)
5. Trovamax IP Phones (this is the main VoIP phone we sell)
6. ovaro phones (to be on a landing page only not apart of the main site)
7. selected headsets from Crandolite (products)
8. Brivasc Conference phone (VoIP model only)
9. we can supply fax to email service

we would like a support page with user guides (step by step instructions on our products and services and FAQ's about all products and services

we have a carrier grade softswitch (telco billing system) k9tally http://www.k9tallyhub.org this system has a ticketing system, customer and agent login I would like a URL link from our website so customers can login to this system. also it is possible to skin k9tally to look like our website

VoIP business plans

$0 per month
call rate .12c land line calls
.24c per minute mobile calls

$25 per month
250 Free local land line calls
call rate is .10c land line calls .22c per minute mobile calls

$50 per month
500 Free local land line calls
call rate .09 land line calls .20c per minute mobile calls

$100 per month
1000 free local land line calls
call rate .08c land line calls .18c per minute mobile calls

all mobile calls are billed per second no flag fall

also require a link to international call rates

We can port your existing telephone number from any carrier or supply new Australian telephone numbers

02, 03, 07, 08, 131, 1300, 1800

Designs i like www.quibrix.com.au and www.sundrapex.com

I would like the website to be white and bright
Updates

Reason: Please use images of the products I sell only

Target Market(s)

business customers only

Requirements
Must have
• all pages must have its own banner to reflect the product or service we are selling. the home page can automatically change to show all pages with a link straight to the page in question

for example if on the home page the banner for trovamax phone is displaying if someone click on the banner they will be redirected to the trovamax page

Must Be SEO friendly
Nice to have
• shopping cart via koinova for all products but before customer checks out i would like to offer two options

1. Pre configure the item and ship to your address for existing customers
2. would you like a ferndale comms technician to attend your office and install the item in person (costs involved $60 call out fee $120 per hours every item sold charge .50 hour and only the one call out fee)

new and existing customers can book service work via the website
1. describe the work required (maybe we need to give a few option)
2. company details
3. pre payment (checkout via koinova) can we put the koinova fees back on to the customer?

```html
<!DOCTYPE html>
<html lang="en">
<head>
<meta charset="utf-8">
<title>Ferndale Comms – Business Phone Systems &amp; Hosted PBX</title>
<link rel="stylesheet" href="https://fonts.googleapis.com/css2?family=Open+Sans:wght@400;600&family=PT+Sans+Narrow:wght@700&display=swap">
<style>
:root{
  --brand:#1d4f8f;
  --brand-dark:#173a63;
  --nav-blue:#1f5fae;
  --ink:#444b55;
  --muted:#8a9099;
  --line:#dcdfe3;
  --card-border:#e4e6e9;
  --btn-bg:#eeeff1;
  --page:#ffffff;
  --hero-top:#ffffff;
  --hero-bottom:#e9ebee;
}
*{box-sizing:border-box;margin:0;padding:0}
html,body{width:1200px;height:2313px;overflow:hidden;background:var(--page)}
body{position:relative;font-family:"Open Sans",Arial,sans-serif;color:var(--ink)}
a{text-decoration:none;color:inherit}

/* top navigation */
.top-nav{position:absolute;left:0;top:0;width:1200px;height:36px;border-bottom:1px solid var(--line);
  display:flex;align-items:center;padding:0 85px;justify-content:space-between;font-size:14px;color:var(--nav-blue);font-weight:600}
.top-nav .sep{width:2px;height:14px;background:var(--nav-blue);opacity:.7}

/* header */
.site-header{position:absolute;left:0;top:37px;width:1200px;height:144px;border-bottom:1px solid var(--line)}
.brand-name{position:absolute;left:80px;top:42px;font-size:40px;font-weight:600;color:var(--brand);letter-spacing:-.5px}
.login{position:absolute;left:745px;top:32px;display:flex;gap:11px}
.login .field{height:29px;border:1px solid var(--line);font-size:11px;color:#b3b7bd;padding:6px 8px;background:#fff}
.login .user{width:149px}.login .pass{width:144px}
.login .go{width:54px;height:29px;border:1px solid #cfd2d6;background:var(--btn-bg);font-size:12px;color:var(--ink);display:flex;align-items:center;justify-content:center}
.hotline{position:absolute;left:962px;top:78px;display:flex;align-items:center;gap:12px;font-size:17px;color:#666}

/* hero */
.hero{position:absolute;left:0;top:185px;width:1200px;height:452px;background:linear-gradient(var(--hero-top) 55%,var(--hero-bottom));border-bottom:1px solid var(--line);overflow:hidden}
.hero-title{position:absolute;left:372px;top:50px;font-family:"PT Sans Narrow",Arial,sans-serif;font-weight:700;font-size:43px;color:var(--brand-dark)}
.hero-person{position:absolute;left:0;top:40px;width:390px;height:412px;background:linear-gradient(135deg,#e9d5c6,#b07c62 60%,#5b3a2c)}
.hero-product{position:absolute;left:848px;top:144px;width:334px;height:295px;border-radius:10px;background:linear-gradient(160deg,#55595f,#1e2024 70%);}
.hero-dots{position:absolute;left:545px;top:420px;display:flex;gap:8px}
.hero-dots span{width:14px;height:14px;border-radius:50%;background:#cfd3d8}
.hero-dots span.on{background:var(--brand)}

/* intro */
.intro{position:absolute;left:85px;top:685px;width:1030px}
.intro h1{font-size:27px;font-weight:400;color:var(--brand-dark)}
.intro .lead{margin-top:20px;width:560px;font-size:17px;line-height:28px;color:var(--muted)}
.intro ul{margin-top:34px;list-style:none;font-size:13px;color:#6c727a}
.intro li{position:relative;padding-left:30px;height:26px;line-height:26px}
.intro li::before{content:"";position:absolute;left:11px;top:11px;width:5px;height:5px;border-radius:50%;background:var(--brand)}

.btn-more{display:inline-flex;align-items:center;gap:12px;height:32px;padding:0 18px 0 14px;background:var(--btn-bg);border-radius:3px;font-size:13px;color:#666}
.btn-more svg{flex:none}
.intro .btn-more{margin-top:30px}

/* product grid */
.products{position:absolute;left:80px;top:1123px;width:1035px;display:grid;grid-template-columns:repeat(3,336px);column-gap:13px;row-gap:31px}
.card{position:relative;height:216px;border:1px solid var(--card-border);box-shadow:0 2px 5px rgba(0,0,0,.06);background:#fff}
.card h2{position:absolute;left:16px;top:16px;display:flex;align-items:center;gap:10px;font-family:"PT Sans Narrow",Arial,sans-serif;font-weight:700;font-size:21px;color:var(--brand-dark);white-space:nowrap}
.card .shot{position:absolute;left:12px;top:70px;width:92px;height:70px;border-radius:6px;background:linear-gradient(160deg,#6b6f75,#2a2c30)}
.card p{position:absolute;left:120px;top:62px;width:205px;font-size:11.5px;line-height:17px;color:var(--muted)}
.card .btn-more{position:absolute;left:197px;top:175px;height:30px;padding:0 16px 0 14px;font-size:12px}

.rule{position:absolute;left:80px;width:1035px;height:1px;background:var(--line)}

/* feature */
.feature-shot{position:absolute;left:80px;top:1910px;width:331px;height:146px;border:1px solid var(--card-border);background:linear-gradient(160deg,#f4f5f6,#c9ccd0)}
.feature-text{position:absolute;left:442px;top:1910px;width:673px;font-size:13px;line-height:19px;color:var(--muted)}
.feature-text p+p{margin-top:19px}
.feature-btn{position:absolute;left:442px;top:2104px}

/* footer */
.footer-nav{position:absolute;left:0;top:2200px;width:1200px;text-align:center;font-size:13px;color:#7a8088;letter-spacing:.3px}
.footer-nav .bar{margin:0 6px;color:#b5b9be}
.copyright{position:absolute;left:80px;top:2264px;font-size:11px;color:#9aa0a6}
.social{position:absolute;left:930px;top:2256px;display:flex;gap:12px}
.social span{width:30px;height:30px;border-radius:4px;background:linear-gradient(#f3f4f5,#d9dcdf);border:1px solid #cfd2d6}
</style>
</head>
<body>

<nav class="top-nav">
  <a href="#">Home</a><span class="sep"></span>
  <a href="#">Products</a><span class="sep"></span>
  <a href="#">About</a><span class="sep"></span>
  <a href="#">Hosted PBX</a><span class="sep"></span>
  <a href="#">Contact Us</a><span class="sep"></span>
  <a href="#">Telephone Systems</a><span class="sep"></span>
  <a href="#">Plans &amp; Signup</a>
</nav>

<header class="site-header">
  <div class="brand-name">ferndale comms</div>
  <form class="login">
    <div class="field user">User Name</div>
    <div class="field pass">Password</div>
    <div class="go">Login</div>
  </form>
  <div class="hotline">
    <svg width="40" height="40" viewBox="0 0 40 40" aria-hidden="true">
      <path d="M8 22a12 12 0 0 1 24 0" fill="none" stroke="#3a3d42" stroke-width="4"/>
      <rect x="4" y="20" width="8" height="13" rx="3" fill="#3a3d42"/>
      <rect x="28" y="20" width="8" height="13" rx="3" fill="#3a3d42"/>
      <path d="M32 32q0 6-10 6" fill="none" stroke="#3a3d42" stroke-width="2"/>
    </svg>
    <span>1300 482 617</span>
  </div>
</header>

<section class="hero">
  <div class="hero-person" role="img" aria-label="Photo of a smiling support agent wearing a headset"></div>
  <div class="hero-title">Very Easily Connect With Everyone...</div>
  <div class="hero-product" role="img" aria-label="Photo of a Trovamax cordless IP phone on its base station"></div>
  <div class="hero-dots"><span class="on"></span><span></span><span></span><span></span><span></span></div>
</section>

<section class="intro">
  <h1>Small to Medium Business Phone Systems &amp; Hosted PBX Solutions</h1>
  <p class="lead">Ferndale Comms can get you started with a feature rich and low upfront cost VoIP Phone System.</p>
  <ul>
    <li>Low upfront phone system costs to get started – from $0.09c</li>
    <li>Self manage your VoIP phone system via friendly web interface</li>
    <li>Smartphone/laptop phone system integration</li>
    <li>No on site technician charges</li>
    <li>Always be up to date with phone system technology</li>
    <li>Link multiple office/home together as one</li>
  </ul>
  <a class="btn-more" href="#"><svg width="10" height="12" viewBox="0 0 10 12"><path d="M0 0l10 6-10 6z" fill="#1d4f8f"/></svg>Learn More</a>
</section>

<section class="products">
  <article class="card"><h2><svg width="18" height="16" viewBox="0 0 18 16"><path d="M1 8l5 6L17 1" fill="none" stroke="#8a9099" stroke-width="3"/></svg>VOIP PROVIDER</h2>
    <div class="shot" role="img" aria-label="Photo of a desk IP phone"></div>
    <p>Lorem ipsum dolor sit amet, consectetuer adipiscing elit. Aenean commodo ligula eget dolor. Aenean massa. Cum sociis natoque penatibus et magnis dis parturient.</p>
    <a class="btn-more" href="#"><svg width="10" height="12" viewBox="0 0 10 12"><path d="M0 0l10 6-10 6z" fill="#1d4f8f"/></svg>Learn More</a></article>
  <article class="card"><h2><svg width="18" height="16" viewBox="0 0 18 16"><path d="M1 8l5 6L17 1" fill="none" stroke="#8a9099" stroke-width="3"/></svg>HOSTED PBX</h2>
    <div class="shot" role="img" aria-label="Photo of a desk IP phone"></div>
    <p>Lorem ipsum dolor sit amet, consectetuer adipiscing elit. Aenean commodo ligula eget dolor. Aenean massa. Cum sociis natoque penatibus et magnis dis parturient.</p>
    <a class="btn-more" href="#"><svg width="10" height="12" viewBox="0 0 10 12"><path d="M0 0l10 6-10 6z" fill="#1d4f8f"/></svg>Learn More</a></article>
  <article class="card"><h2><svg width="18" height="16" viewBox="0 0 18 16"><path d="M1 8l5 6L17 1" fill="none" stroke="#8a9099" stroke-width="3"/></svg>NOLVAR IP PBX</h2>
    <div class="shot" role="img" aria-label="Photo of a desk IP phone"></div>
    <p>Lorem ipsum dolor sit amet, consectetuer adipiscing elit. Aenean commodo ligula eget dolor. Aenean massa. Cum sociis natoque penatibus et magnis dis parturient.</p>
    <a class="btn-more" href="#"><svg width="10" height="12" viewBox="0 0 10 12"><path d="M0 0l10 6-10 6z" fill="#1d4f8f"/></svg>Learn More</a></article>
  <article class="card"><h2><svg width="18" height="16" viewBox="0 0 18 16"><path d="M1 8l5 6L17 1" fill="none" stroke="#8a9099" stroke-width="3"/></svg>DALQON IP PBX</h2>
    <div class="shot" role="img" aria-label="Photo of a desk IP phone"></div>
    <p>Lorem ipsum dolor sit amet, consectetuer adipiscing elit. Aenean commodo ligula eget dolor. Aenean massa. Cum sociis natoque penatibus et magnis dis parturient.</p>
    <a class="btn-more" href="#"><svg width="10" height="12" viewBox="0 0 10 12"><path d="M0 0l10 6-10 6z" fill="#1d4f8f"/></svg>Learn More</a></article>
  <article class="card"><h2><svg width="18" height="16" viewBox="0 0 18 16"><path d="M1 8l5 6L17 1" fill="none" stroke="#8a9099" stroke-width="3"/></svg>TROVAMAX IP PHONES</h2>
    <div class="shot" role="img" aria-label="Photo of a desk IP phone"></div>
    <p>Lorem ipsum dolor sit amet, consectetuer adipiscing elit. Aenean commodo ligula eget dolor. Aenean massa. Cum sociis natoque penatibus et magnis dis parturient.</p>
    <a class="btn-more" href="#"><svg width="10" height="12" viewBox="0 0 10 12"><path d="M0 0l10 6-10 6z" fill="#1d4f8f"/></svg>Learn More</a></article>
  <article class="card"><h2><svg width="18" height="16" viewBox="0 0 18 16"><path d="M1 8l5 6L17 1" fill="none" stroke="#8a9099" stroke-width="3"/></svg>OVARO PHONES</h2>
    <div class="shot" role="img" aria-label="Photo of a desk IP phone"></div>
    <p>Lorem ipsum dolor sit amet, consectetuer adipiscing elit. Aenean commodo ligula eget dolor. Aenean massa. Cum sociis natoque penatibus et magnis dis parturient.</p>
    <a class="btn-more" href="#"><svg width="10" height="12" viewBox="0 0 10 12"><path d="M0 0l10 6-10 6z" fill="#1d4f8f"/></svg>Learn More</a></article>
  <article class="card"><h2><svg width="18" height="16" viewBox="0 0 18 16"><path d="M1 8l5 6L17 1" fill="none" stroke="#8a9099" stroke-width="3"/></svg>HEADSET PRODUCTS</h2>
    <div class="shot" role="img" aria-label="Photo of a desk IP phone"></div>
    <p>Lorem ipsum dolor sit amet, consectetuer adipiscing elit. Aenean commodo ligula eget dolor. Aenean massa. Cum sociis natoque penatibus et magnis dis parturient.</p>
    <a class="btn-more" href="#"><svg width="10" height="12" viewBox="0 0 10 12"><path d="M0 0l10 6-10 6z" fill="#1d4f8f"/></svg>Learn More</a></article>
  <article class="card"><h2><svg width="18" height="16" viewBox="0 0 18 16"><path d="M1 8l5 6L17 1" fill="none" stroke="#8a9099" stroke-width="3"/></svg>BRIVASC CONFERENCE PHON</h2>
    <div class="shot" role="img" aria-label="Photo of a desk IP phone"></div>
    <p>Lorem ipsum dolor sit amet, consectetuer adipiscing elit. Aenean commodo ligula eget dolor. Aenean massa. Cum sociis natoque penatibus et magnis dis parturient.</p>
    <a class="btn-more" href="#"><svg width="10" height="12" viewBox="0 0 10 12"><path d="M0 0l10 6-10 6z" fill="#1d4f8f"/></svg>Learn More</a></article>
  <article class="card"><h2><svg width="18" height="16" viewBox="0 0 18 16"><path d="M1 8l5 6L17 1" fill="none" stroke="#8a9099" stroke-width="3"/></svg>FAX TO EMAIL SERVICE</h2>
    <div class="shot" role="img" aria-label="Photo of a desk IP phone"></div>
    <p>Lorem ipsum dolor sit amet, consectetuer adipiscing elit. Aenean commodo ligula eget dolor. Aenean massa. Cum sociis natoque penatibus et magnis dis parturient.</p>
    <a class="btn-more" href="#"><svg width="10" height="12" viewBox="0 0 10 12"><path d="M0 0l10 6-10 6z" fill="#1d4f8f"/></svg>Learn More</a></article>
</section>

<div class="rule" style="top:1876px"></div>

<div class="feature-shot" role="img" aria-label="Photo of a Trovamax desk IP phone with display"></div>
<div class="feature-text">
  <p>Donec quam felis, ultricies nec, pellentesque eu, pretium quis, sem. Nulla consequat massa quis enim. Donec pede justo, fringilla vel, aliquet nec, vulputate eget, arcu. In enim justo, rhoncus ut, imperdiet a, venenatis vitae, justo. Nullam dictum felis eu pede mollis pretium. Lorem ipsum dolor sit amet, consectetuer adipiscing elit. Aenean commodo ligula eget dolor.</p>
  <p>Donec quam felis, ultricies nec, pellentesque eu, pretium quis, sem. Nulla consequat massa quis enim. Donec pede justo, fringilla vel, aliquet nec, vulputate eget, arcu. In enim justo, rhoncus ut, imperdiet a, venenatis vitae, justo. Nullam dictum felis eu pede mollis pretium. Lorem ipsum dolor sit amet, consectetuer adipiscing elit. Aenean commodo ligula eget dolor.</p>
</div>
<a class="btn-more feature-btn" href="#"><svg width="10" height="12" viewBox="0 0 10 12"><path d="M0 0l10 6-10 6z" fill="#1d4f8f"/></svg>Learn More</a>

<div class="rule" style="top:2180px;left:0;width:1200px"></div>
<footer>
  <nav class="footer-nav">
    <a href="#">Home</a><span class="bar">|</span><a href="#">Products</a><span class="bar">|</span><a href="#">About</a><span class="bar">|</span><a href="#">Hosted PBX</a><span class="bar">|</span><a href="#">Contact Us</a><span class="bar">|</span><a href="#">Telephone Systems</a><span class="bar">|</span><a href="#">Plans &amp; Signup</a>
  </nav>
  <div class="rule" style="top:2241px;left:0;width:1200px"></div>
  <p class="copyright">Copyright © 2013 ferndale comms</p>
  <div class="social"><span></span><span></span><span></span><span></span><span></span></div>
</footer>

</body>
</html>
```